Harborvale Ventures brochure for Investment partnership, young harold pembly

We need a brochure design to attract new investors for our investing partnership Called Harborvale Ventures. We are based in New Orleans, La. We primarily invest in stocks, bonds, and crypto but venture out into other categories as well. We would like to see designs with the black and gold like our logo. The final design should say new, fresh, sleek, tech, and honorable. BROUCHURE WILL BE 4 pages.or one folded sheet a paparer if that makes sense.
Updates

A chart showing Harborvale Ventures gains since 2019 28.6 percent and the TR 400 gAINS 7.1 PERCENT

Target Market(s)

Probable Investors

Industry/Entity Type

Financial Planning

Colors

Designer to choose only greyscale colors for use in the design.

Requirements
Must have
• Black and Gold accent. Stock market feel. Sleek, High tech, innovative, Intellgent design.
Nice to have
• Page colors possibly black.
Should not have
• Boring, Old school,

```html
<!DOCTYPE html>
<html lang="en">
<head>
<meta charset="UTF-8">
<title>Harborvale Ventures – Investor Brochure</title>
<link rel="stylesheet" href="https://fonts.googleapis.com/css2?family=Cinzel:wght@600;700&family=Playfair+Display:wght@400;600&family=Montserrat:wght@400;600;700;800&display=swap">
<style>
  :root {
    --canvas: #d4d4d4;
    --paper: #ffffff;
    --ink: #141414;
    --black: #0b0b0b;
    --gold: #c8a24a;
    --gold-light: #e2c476;
    --grey-text: #6b6b6b;
    --grey-bar: #9a9a9a;
    --rule: #dcdcdc;
  }
  * { box-sizing: border-box; margin: 0; padding: 0; }
  html, body { width: 865px; height: 1200px; overflow: hidden; }
  body {
    background: var(--canvas);
    font-family: "Montserrat", sans-serif;
    color: var(--ink);
    position: relative;
  }
  .spread {
    position: absolute;
    left: 52px;
    width: 760px;
    height: 537px;
    display: flex;
    box-shadow: 0 6px 18px rgba(0,0,0,.18);
  }
  .spread--covers { top: 40px; }
  .spread--inside { top: 622px; }
  .page {
    position: relative;
    width: 380px;
    height: 537px;
    overflow: hidden;
    background: var(--paper);
  }
  .page + .page { border-left: 1px solid #e6e6e6; }

  /* Back cover */
  .about { padding: 34px 30px 0; }
  .about__title { font-size: 17px; font-weight: 800; letter-spacing: 2px; }
  .about__subtitle {
    margin-top: 4px; font-size: 7.5px; font-weight: 700; letter-spacing: 1px;
    color: var(--gold); text-transform: uppercase;
  }
  .about__rule { width: 46px; height: 2px; background: var(--gold); margin: 10px 0 12px; }
  .about__text { font-size: 8px; line-height: 1.6; color: var(--grey-text); width: 290px; }
  .about__photo {
    margin-top: 16px; width: 320px; height: 170px;
    background: linear-gradient(160deg, #bdbdbd 0%, #7a7a7a 55%, #3c3c3c 100%);
  }
  .contact { margin-top: 22px; list-style: none; }
  .contact__item {
    display: flex; align-items: center; gap: 9px;
    font-size: 8px; color: var(--grey-text); margin-bottom: 9px;
  }
  .contact__icon { width: 16px; height: 16px; flex: none; }

  /* Front cover */
  .cover { background: var(--black); color: #fff; }
  .cover__masthead {
    height: 62px; display: flex; align-items: center; justify-content: center; gap: 8px;
  }
  .brand-name {
    font-family: "Cinzel", serif; font-weight: 700; color: var(--gold);
    letter-spacing: 2px; text-transform: uppercase;
  }
  .brand-mark { width: 9px; height: 9px; background: var(--gold); }
  .cover__masthead .brand-name { font-size: 19px; }
  .cover__photo {
    height: 236px;
    background: linear-gradient(135deg, #1a2633 0%, #3e5670 45%, #9fb3c6 70%, #2a3a4c 100%);
  }
  .cover__headline {
    height: 118px; display: flex; align-items: center; justify-content: center;
    text-align: center; padding: 0 44px;
    font-family: "Playfair Display", serif; font-weight: 600; font-size: 15px; line-height: 1.45;
  }
  .cover__tagline {
    height: 28px; background: var(--gold); color: var(--black);
    display: flex; align-items: center; justify-content: center;
    font-size: 9px; font-weight: 700; letter-spacing: 1px; text-transform: uppercase;
  }
  .cover__footer {
    height: 93px; display: flex; flex-direction: column; align-items: center;
    justify-content: center; gap: 8px;
  }
  .cover__footer .brand-name { font-size: 11px; }
  .cover__web { font-size: 7.5px; letter-spacing: 2px; color: #cfcfcf; }

  /* Inside left */
  .feature-photo {
    position: absolute; inset: 0 0 108px 0;
    background: linear-gradient(180deg, #d8d8d8 0%, #8e8e8e 40%, #4a4a4a 75%, #262626 100%);
  }
  .consult {
    position: absolute; left: 0; right: 0; bottom: 0; height: 108px;
    background: var(--black); display: flex; align-items: center; gap: 14px; padding: 0 28px;
  }
  .consult__icon { width: 42px; height: 42px; flex: none; }
  .consult__label {
    color: #fff; font-size: 10px; font-weight: 700; letter-spacing: 1.5px;
    line-height: 1.5; text-transform: uppercase;
  }
  .consult__label strong { color: var(--gold); }
  .consult__phone { color: var(--gold); font-size: 24px; font-weight: 800; letter-spacing: 1px; margin-top: 2px; }

  /* Inside right */
  .steps { padding: 34px 30px 0; }
  .steps__title { font-size: 17px; font-weight: 800; letter-spacing: 2px; }
  .steps__rule { width: 46px; height: 2px; background: var(--gold); margin: 10px 0 16px; }
  .steps__list { list-style: none; }
  .step { display: flex; gap: 12px; align-items: flex-start; margin-bottom: 12px; }
  .step__num {
    width: 24px; height: 24px; border-radius: 50%; background: var(--gold); flex: none;
    color: var(--black); font-size: 10px; font-weight: 800;
    display: flex; align-items: center; justify-content: center;
  }
  .step__text { font-size: 8px; line-height: 1.6; color: var(--grey-text); padding-top: 3px; }

  .gains {
    position: absolute; left: 30px; right: 30px; top: 200px; height: 150px;
    background: var(--black); padding: 12px 16px 10px;
  }
  .gains__title {
    font-size: 8.5px; font-weight: 700; letter-spacing: 1.5px; color: var(--gold);
    text-transform: uppercase;
  }
  .gains__chart { display: block; width: 288px; height: 112px; margin-top: 6px; }

  .app-photo {
    position: absolute; left: 30px; right: 0; bottom: 0; height: 172px;
    background: linear-gradient(140deg, #0e1a22 0%, #1f3a4a 45%, #2f6b5e 70%, #0c1418 100%);
  }
</style>
</head>
<body>

<section class="spread spread--covers">
  <article class="page page--back">
    <div class="about">
      <h2 class="about__title">ABOUT</h2>
      <p class="about__subtitle">Harborvale Ventures: Your Investment Partner</p>
      <div class="about__rule"></div>
      <p class="about__text">We are a private partnership based in New Orleans, investing in stocks, bonds and crypto with a disciplined, long-term approach built on trust.</p>
      <div class="about__photo" role="img" aria-label="Black and white photo of a New Orleans streetcar on a city street"></div>
      <ul class="contact">
        <li class="contact__item">
          <svg class="contact__icon" viewBox="0 0 16 16"><circle cx="8" cy="8" r="8" fill="#c8a24a"/><path d="M8 3.5a2.6 2.6 0 0 0-2.6 2.6C5.4 8.2 8 12 8 12s2.6-3.8 2.6-5.9A2.6 2.6 0 0 0 8 3.5z" fill="#fff"/><circle cx="8" cy="6.1" r="1" fill="#c8a24a"/></svg>
          <span>1200 Harbor Street, New Orleans, LA</span>
        </li>
        <li class="contact__item">
          <svg class="contact__icon" viewBox="0 0 16 16"><circle cx="8" cy="8" r="8" fill="#c8a24a"/><path d="M5.4 4.2l1.4-.3.8 2-.9.7a5 5 0 0 0 2.7 2.7l.7-.9 2 .8-.3 1.4c-3.6.4-6.8-2.8-6.4-6.4z" fill="#fff"/></svg>
          <span>(504) 555-0142</span>
        </li>
        <li class="contact__item">
          <svg class="contact__icon" viewBox="0 0 16 16"><circle cx="8" cy="8" r="8" fill="#c8a24a"/><rect x="4" y="5" width="8" height="6" fill="#fff"/><path d="M4 5l4 3.2L12 5" fill="none" stroke="#c8a24a" stroke-width=".8"/></svg>
          <span>info@harborvaleventures.com</span>
        </li>
        <li class="contact__item">
          <svg class="contact__icon" viewBox="0 0 16 16"><circle cx="8" cy="8" r="8" fill="#c8a24a"/><circle cx="8" cy="8" r="3.6" fill="none" stroke="#fff" stroke-width=".9"/><path d="M4.4 8h7.2M8 4.4c-1.6 2.2-1.6 5 0 7.2M8 4.4c1.6 2.2 1.6 5 0 7.2" fill="none" stroke="#fff" stroke-width=".7"/></svg>
          <span>www.harborvaleventures.com</span>
        </li>
      </ul>
    </div>
  </article>

  <article class="page cover">
    <header class="cover__masthead">
      <span class="brand-mark"></span>
      <span class="brand-name">Harborvale Ventures</span>
    </header>
    <div class="cover__photo" role="img" aria-label="Businessman in a suit using a tablet against a city skyline"></div>
    <h1 class="cover__headline">Become a Partner and Build Consistent Wealth By Investing In The Stock Market</h1>
    <p class="cover__tagline">A Fresh Take On Private Investment Capital</p>
    <footer class="cover__footer">
      <span class="brand-name">Harborvale Ventures</span>
      <span class="cover__web">www.harborvaleventures.com</span>
    </footer>
  </article>
</section>

<section class="spread spread--inside">
  <article class="page page--feature">
    <div class="feature-photo" role="img" aria-label="Black and white photo of a historic New Orleans house with iron balconies"></div>
    <div class="consult">
      <svg class="consult__icon" viewBox="0 0 42 42"><circle cx="21" cy="21" r="20" fill="#c8a24a"/><path d="M14 11.5l3.6-.8 2 5-2.3 1.8a13 13 0 0 0 7.2 7.2l1.8-2.3 5 2-.8 3.6c-9.4 1-17.5-7.1-16.5-16.5z" fill="#0b0b0b"/></svg>
      <div>
        <p class="consult__label">Call us now<br><strong>For a free consultation</strong></p>
        <p class="consult__phone">0100 555 0199</p>
      </div>
    </div>
  </article>

  <article class="page page--steps">
    <div class="steps">
      <h2 class="steps__title">HOW IT WORKS</h2>
      <div class="steps__rule"></div>
      <ol class="steps__list">
        <li class="step"><span class="step__num">1</span><p class="step__text">Meet with our team to discuss your goals and investment horizon.</p></li>
        <li class="step"><span class="step__num">2</span><p class="step__text">Join the partnership with a capital commitment that suits you.</p></li>
        <li class="step"><span class="step__num">3</span><p class="step__text">Track your growth with clear quarterly reports and updates.</p></li>
      </ol>
    </div>

    <figure class="gains">
      <figcaption class="gains__title">Gains Since 2019</figcaption>
      <svg class="gains__chart" viewBox="0 0 288 112" role="img" aria-label="Bar chart: Harborvale Ventures gained 28.6 percent, TR 400 gained 7.1 percent since 2019">
        <g font-family="Montserrat, sans-serif">
          <line x1="0" y1="92" x2="288" y2="92" stroke="#444" stroke-width="1"/>
          <line x1="0" y1="62" x2="288" y2="62" stroke="#222" stroke-width=".6"/>
          <line x1="0" y1="32" x2="288" y2="32" stroke="#222" stroke-width=".6"/>
          <rect x="46" y="20" width="62" height="72" fill="#c8a24a"/>
          <text x="77" y="14" text-anchor="middle" font-size="12" font-weight="800" fill="#c8a24a">28.6%</text>
          <rect x="180" y="74" width="62" height="18" fill="#9a9a9a"/>
          <text x="211" y="68" text-anchor="middle" font-size="12" font-weight="800" fill="#ffffff">7.1%</text>
          <text x="77" y="106" text-anchor="middle" font-size="7.5" font-weight="700" letter-spacing=".8" fill="#ffffff">HARBORVALE VENTURES</text>
          <text x="211" y="106" text-anchor="middle" font-size="7.5" font-weight="700" letter-spacing=".8" fill="#ffffff">TR 400</text>
        </g>
      </svg>
    </figure>

    <div class="app-photo" role="img" aria-label="Hands holding a smartphone showing a stock market trading chart"></div>
  </article>
</section>

</body>
</html>
```